Visitenkarten für eine Hypnose-Praxis
Ich bin sehr zufrieden mit der professionellen Arbeitsweise von KOR7342. Es war immer ein netter Kontakt und meine Wünsche wurden schnell umgesetzt. Alle Vorschläge waren sehr kreativ und und so viel es mir leicht, eine schnelle Entscheidung zu treffen.
Zielgruppe
Wir sind eine Hypnose-Praxis und richten unser Angebot an Privatpersonen unterschiedlichen Alters, die therapeutische Unterstützung suchen.
Aufgabenstellung
Eher schlichtes und modernes Design

```html
<!DOCTYPE html>
<html lang="de">
<head>
<meta charset="utf-8">
<title>seelenruh – Visitenkarte</title>
<link rel="stylesheet" href="https://fonts.googleapis.com/css2?family=Lato:wght@300;400&display=swap">
<style>
  :root {
    --backdrop: #d9d9d9;
    --card: #ffffff;
    --ink: #222222;
    --muted: #7a7a7a;
    --icon: #8a8a8a;
    --accent: #4aa8c4;
  }
  * { margin: 0; padding: 0; box-sizing: border-box; }
  html, body {
    width: 1200px;
    height: 525px;
    overflow: hidden;
    background: var(--backdrop);
    font-family: "Lato", "Helvetica Neue", Arial, sans-serif;
  }
  .business-card {
    position: absolute;
    left: 190px;
    top: 22px;
    width: 820px;
    height: 480px;
    background: var(--card);
  }
  .brand {
    position: absolute;
    left: 100px;
    top: 95px;
    display: flex;
    align-items: center;
    gap: 26px;
  }
  .brand-square {
    width: 58px;
    height: 58px;
    background: var(--accent);
    border-radius: 6px;
  }
  .brand-text { display: flex; flex-direction: column; }
  .brand-name {
    font-size: 84px;
    font-weight: 400;
    line-height: 1;
    color: var(--ink);
    letter-spacing: -1px;
  }
  .brand-tagline {
    margin-top: 10px;
    font-size: 21px;
    font-weight: 300;
    letter-spacing: 4px;
    color: var(--muted);
  }
  .intro {
    position: absolute;
    left: 72px;
    top: 368px;
    width: 420px;
    font-size: 17px;
    font-weight: 400;
    line-height: 1.5;
    color: var(--muted);
  }
  .contact-list {
    position: absolute;
    left: 488px;
    top: 366px;
    list-style: none;
    font-size: 16px;
    color: #555;
  }
  .contact-item {
    display: flex;
    align-items: center;
    gap: 14px;
    height: 27px;
  }
  .contact-icon { width: 18px; height: 18px; fill: var(--icon); flex: none; }
</style>
</head>
<body>
  <main class="business-card">
    <div class="brand">
      <div class="brand-square" aria-hidden="true"></div>
      <div class="brand-text">
        <span class="brand-name">seelenruh</span>
        <span class="brand-tagline">HYPNOSE-THERAPIE</span>
      </div>
    </div>

    <p class="intro">Wir sind eine Hypnose-Praxis und unser Angebot an Privatpersonen unterschiedlichen Alters, die Unterstützung suchen.</p>

    <ul class="contact-list">
      <li class="contact-item">
        <svg class="contact-icon" viewBox="0 0 24 24" aria-hidden="true"><path d="M6.6 10.8a15.1 15.1 0 0 0 6.6 6.6l2.2-2.2c.3-.3.7-.4 1-.2 1.1.4 2.3.6 3.6.6.6 0 1 .4 1 1V20c0 .6-.4 1-1 1A17 17 0 0 1 3 4c0-.6.4-1 1-1h3.5c.6 0 1 .4 1 1 0 1.3.2 2.5.6 3.6.1.3 0 .7-.2 1z"/></svg>
        <span>+49 321 987654</span>
      </li>
      <li class="contact-item">
        <svg class="contact-icon" viewBox="0 0 24 24" aria-hidden="true"><path d="M3 5h18v14H3zM5 7v.4l7 4.6 7-4.6V7zm0 2.8V17h14V9.8l-7 4.6z"/></svg>
        <span>info</span>
      </li>
      <li class="contact-item">
        <svg class="contact-icon" viewBox="0 0 24 24" aria-hidden="true"><path d="M12 2a10 10 0 1 0 0 20 10 10 0 0 0 0-20zm6.9 6h-3a15 15 0 0 0-1.3-3.6A8 8 0 0 1 18.9 8zM12 4c.8 1.2 1.5 2.5 1.9 4h-3.8c.4-1.5 1.1-2.8 1.9-4zM4.3 14a8 8 0 0 1 0-4h3.4a16 16 0 0 0 0 4zm.8 2h3a15 15 0 0 0 1.3 3.6A8 8 0 0 1 5.1 16zm3-8h-3a8 8 0 0 1 4.3-3.6A15 15 0 0 0 8.1 8zM12 20c-.8-1.2-1.5-2.5-1.9-4h3.8c-.4 1.5-1.1 2.8-1.9 4zm2.3-6H9.7a14 14 0 0 1 0-4h4.6a14 14 0 0 1 0 4zm.3 5.6a15 15 0 0 0 1.3-3.6h3a8 8 0 0 1-4.3 3.6zm1.7-5.6a16 16 0 0 0 0-4h3.4a8 8 0 0 1 0 4z"/></svg>
        <span>www.seelenruh-hypnose.de</span>
      </li>
    </ul>
  </main>
</body>
</html>
```